Copper Lantern Gin

The gin is 100% proof and men and anbody 18 - 30 year old will be a target market - the bottle is very distinctive and lends itself to a square label.

The bottle is curved with a large front face that lends itself to a striking design. There should be enough space around the label to show the black gin in the bottle as this is a feature.

The current bottle with the existing label is attached below as is the new glass bottle. The new gin will be coloured black.

Font styles to use
Decorative
Script

```html
<!DOCTYPE html>
<html lang="en">
<head>
<meta charset="utf-8">
<title>Copper Lantern Gin – Label</title>
<link href="https://fonts.googleapis.com/css2?family=Caveat+Brush&family=Roboto+Slab:wght@500&display=swap" rel="stylesheet">
<style>
  :root {
    --gin-black: #111111;
    --label-white: #ffffff;
    --title-red: #8e1111;
    --ink: #1a1a1a;
    --sketch-grey: #6a6a6a;
  }
  html, body {
    margin: 0;
    padding: 0;
    width: 1200px;
    height: 1200px;
    overflow: hidden;
    background: var(--gin-black);
  }
  .canvas {
    position: relative;
    width: 1200px;
    height: 1200px;
  }
  .label {
    position: absolute;
    left: 150px;
    top: 150px;
    width: 900px;
    height: 900px;
    background: var(--label-white);
  }
  .label__title {
    position: absolute;
    top: 58px;
    left: 0;
    width: 100%;
    margin: 0;
    text-align: center;
    font-family: "Caveat Brush", cursive;
    font-weight: 400;
    font-size: 118px;
    line-height: 112px;
    letter-spacing: 2px;
    text-transform: uppercase;
    color: var(--title-red);
  }
  .label__title span { display: block; }
  .label__illustration {
    position: absolute;
    left: 210px;
    top: 400px;
    width: 470px;
    height: 300px;
  }
  .label__subtitle {
    position: absolute;
    top: 745px;
    left: 0;
    width: 100%;
    margin: 0;
    text-align: center;
    font-family: "Roboto Slab", serif;
    font-weight: 500;
    font-size: 31px;
    letter-spacing: 2px;
    color: var(--ink);
  }
  .label__volume,
  .label__abv {
    position: absolute;
    top: 812px;
    margin: 0;
    font-family: "Roboto Slab", serif;
    font-weight: 500;
    font-size: 26px;
    letter-spacing: 1px;
    color: var(--ink);
  }
  .label__volume { left: 63px; }
  .label__abv { right: 68px; }
</style>
</head>
<body>
<main class="canvas">
  <section class="label">
    <h1 class="label__title">
      <span>Copper</span>
      <span>Lantern</span>
      <span>Gin</span>
    </h1>
    <svg class="label__illustration" viewBox="0 0 470 300" role="img" aria-label="Ink sketch of a black hound running to the right">
      <defs>
        <radialGradient id="sketch-fill" cx="50%" cy="55%" r="55%">
          <stop offset="0%" stop-color="#2a2a2a"/>
          <stop offset="70%" stop-color="#8a8a8a" stop-opacity="0.5"/>
          <stop offset="100%" stop-color="#ffffff" stop-opacity="0"/>
        </radialGradient>
      </defs>
      <rect width="470" height="300" fill="url(#sketch-fill)"/>
    </svg>
    <p class="label__subtitle">NAVY STRENGTH BRITISH GIN</p>
    <p class="label__volume">50CL</p>
    <p class="label__abv">57%ABV</p>
  </section>
</main>
</body>
</html>
```